Australian Software Consultancy needs new Business Card Design

Design Business Card based on existing design artefacts (attached). We are open to all designs. As its a 2 sided design and we thought it might be quite striking to have one side with a black background and te other side with a white background.

Target Market(s)

Financial Services mainly.

Industry/Entity Type

Business

Contact Information for Business Card

Name :
Position :
Email :

Requirements
Must have
• Funky design using our existing assets

```html
<!DOCTYPE html>
<html lang="en">
<head>
<meta charset="utf-8">
<title>Clear Signal – Business Card</title>
<link rel="stylesheet" href="https://fonts.googleapis.com/css2?family=Saira:wght@700&family=Open+Sans:wght@600;700&display=swap">
<style>
  :root {
    --page: #ffffff;
    --ink: #111111;
    --muted: #8a8a8a;
    --accent: #e0262b;
    --card-dark: #06080d;
    --photo-deep: #0a1526;
    --photo-mid: #1d3a63;
    --photo-glow: #8fb3d8;
    --card-edge: #bdbdbd;
  }
  * { box-sizing: border-box; margin: 0; padding: 0; }
  html, body {
    width: 1200px;
    height: 357px;
    overflow: hidden;
    background: var(--page);
  }
  .sheet {
    position: relative;
    width: 1200px;
    height: 357px;
  }
  .side-label {
    position: absolute;
    top: 2px;
    font: 700 15px/20px "Open Sans", sans-serif;
    color: var(--ink);
    transform: translateX(-50%);
  }
  .side-label--front { left: 271px; }
  .side-label--back { left: 927px; }

  .card {
    position: absolute;
    overflow: hidden;
  }

  /* Front */
  .card--front {
    left: 6px;
    top: 50px;
    width: 542px;
    height: 299px;
    background: var(--card-dark);
    border: 1px solid var(--accent);
  }
  .front-photo {
    position: absolute;
    inset: 0 0 64px 0;
    background:
      radial-gradient(circle at 36% 28%, var(--photo-glow) 0%, var(--photo-mid) 18%, transparent 36%),
      radial-gradient(ellipse at 55% 45%, rgba(70,120,180,.5) 0%, transparent 60%),
      linear-gradient(180deg, var(--photo-deep) 0%, #0c1a2e 55%, var(--card-dark) 100%);
  }
  .wordmark {
    position: absolute;
    left: 0;
    right: 0;
    text-align: center;
    font-family: "Saira", sans-serif;
    font-weight: 700;
    letter-spacing: 2px;
    white-space: nowrap;
  }
  .wordmark--front {
    bottom: 8px;
    font-size: 50px;
    line-height: 60px;
    color: #ffffff;
  }

  /* Back */
  .card--back {
    left: 663px;
    top: 46px;
    width: 520px;
    height: 307px;
    background: #ffffff;
    border: 1px solid var(--card-edge);
  }
  .holder {
    position: absolute;
    right: 10px;
    top: 20px;
    text-align: right;
    font-family: "Open Sans", sans-serif;
    color: var(--ink);
  }
  .holder__name { font-size: 15px; font-weight: 700; line-height: 22px; }
  .holder__role { font-size: 12px; font-weight: 700; line-height: 18px; }
  .wordmark--back {
    top: 135px;
    font-size: 54px;
    line-height: 64px;
    color: var(--ink);
  }
  .contact {
    position: absolute;
    left: 0;
    right: 0;
    bottom: 14px;
    text-align: center;
    font: 600 15px/20px "Open Sans", sans-serif;
    color: var(--muted);
  }
</style>
</head>
<body>
<div class="sheet">
  <div class="side-label side-label--front">Front</div>
  <div class="side-label side-label--back">Back</div>

  <section class="card card--front">
    <div class="front-photo" role="img" aria-label="Photo of a glowing globe floating above an open hand among scattered digital screens"></div>
    <div class="wordmark wordmark--front">CLEAR SIGNAL</div>
  </section>

  <section class="card card--back">
    <div class="holder">
      <div class="holder__name">JANE CARTER</div>
      <div class="holder__role">Graphic Designer</div>
    </div>
    <div class="wordmark wordmark--back">CLEAR SIGNAL</div>
    <div class="contact">E-mail : signal@mail.com</div>
  </section>
</div>
</body>
</html>
```